Website with links and a professional business card

Bridging the Financial Gap is our Mission statement or MOTO
Please use my LOGO that was created by Vivid marsh.
We offer Tax & Accounting
We provide Tax Planning
Retirement planning
New business start ups
Payroll
Business Advice and planning
We strive to excellence and convey a family friendly Tax Firm. We offer UDL links to learn more.

Target Market(s)

Tax & Accouting

Industry/Entity Type

Tax & Accounting

Contact Information for Business Card

Classy and elegant for a Women owned Business

Colors

Designer to choose colors to be used in the design.

Requirements
Must have
• Logo, Owners Name, Phone numbers QR code to the website
Nice to have
• My logo center on the card with nice colors that enhance the Silver, Navy blue and red
Should not have
• No currency signs or symbols

```html
<!DOCTYPE html>
<html lang="en">
<head>
<meta charset="utf-8">
<title>Harbor Ledger – Business Card</title>
<link href="https://fonts.googleapis.com/css2?family=Montserrat:wght@400;500;700;800&display=swap" rel="stylesheet">
<style>
  :root {
    --navy: #0d1a45;
    --silver: #8a8a8a;
    --red: #d0202a;
    --paper: #ffffff;
    --backdrop: #c9c8c4;
    --ink: #1f1f1f;
  }
  * { margin: 0; padding: 0; box-sizing: border-box; }
  html, body { width: 1200px; height: 801px; overflow: hidden; }
  body {
    background: var(--backdrop);
    font-family: "Montserrat", sans-serif;
    color: var(--ink);
    position: relative;
  }
  .card {
    position: absolute;
    width: 540px;
    height: 309px;
    background: var(--paper);
    border-bottom: 3px solid var(--red);
    box-shadow: 0 12px 28px rgba(0,0,0,0.22);
  }
  .card--contact { left: 45px; top: 246px; }
  .card--brand { left: 615px; top: 246px; }

  .corner-stripe {
    position: absolute;
    top: 0; right: 0;
    width: 34px; height: 14px;
    background: var(--red);
  }
  .holder { position: absolute; top: 26px; right: 48px; text-align: right; }
  .holder__name { font-weight: 800; font-size: 22px; color: var(--navy); letter-spacing: 0.5px; }
  .holder__title { font-size: 13px; margin-top: 2px; }

  .brand-mark { display: flex; align-items: center; gap: 10px; }
  .brand-mark__dot { border-radius: 50%; background: var(--silver); flex: none; }
  .brand-mark__name { font-weight: 800; color: var(--navy); text-transform: uppercase; letter-spacing: 2px; }

  .card--contact .brand-mark { position: absolute; left: 30px; top: 108px; }
  .card--contact .brand-mark__dot { width: 34px; height: 34px; }
  .card--contact .brand-mark__name { font-size: 24px; }

  .address { position: absolute; left: 30px; top: 170px; font-size: 13px; line-height: 1.35; }
  .contacts { position: absolute; left: 30px; top: 218px; list-style: none; font-size: 13px; }
  .contacts li { display: flex; align-items: center; gap: 8px; line-height: 22px; }
  .contacts svg { width: 14px; height: 14px; flex: none; }

  .card--brand .brand-mark { position: absolute; left: 0; right: 0; top: 0; bottom: 0; justify-content: center; }
  .card--brand .brand-mark__dot { width: 56px; height: 56px; }
  .card--brand .brand-mark__name { font-size: 40px; }
</style>
</head>
<body>
  <section class="card card--contact">
    <div class="corner-stripe"></div>
    <div class="holder">
      <div class="holder__name">CLAIRE WHITFIELD</div>
      <div class="holder__title">Managing Director</div>
    </div>
    <div class="brand-mark">
      <span class="brand-mark__dot"></span>
      <span class="brand-mark__name">Harbor Ledger</span>
    </div>
    <p class="address">Your address, City<br>State, Zip 1234</p>
    <ul class="contacts">
      <li>
        <svg viewBox="0 0 14 14" aria-hidden="true"><circle cx="7" cy="7" r="7" fill="var(--red)"/><path d="M4.2 3.8c.4-.4.9-.3 1.1.1l.6 1.1c.2.4 0 .7-.3.9l-.3.2c.4.9 1 1.5 1.9 1.9l.2-.3c.2-.3.5-.5.9-.3l1.1.6c.4.2.5.7.1 1.1-.7.7-1.7.8-2.6.3C5.6 8.8 4.6 7.8 4 6.5c-.5-.9-.4-1.9.2-2.7z" fill="#fff"/></svg>
        <span>123 456 789</span>
      </li>
      <li>
        <svg viewBox="0 0 14 14" aria-hidden="true"><circle cx="7" cy="7" r="7" fill="var(--red)"/><rect x="3.5" y="4.5" width="7" height="5" fill="none" stroke="#fff" stroke-width="1"/><path d="M3.5 4.5L7 7.3l3.5-2.8" fill="none" stroke="#fff" stroke-width="1"/></svg>
        <span>info@yourmail.com</span>
      </li>
      <li>
        <svg viewBox="0 0 14 14" aria-hidden="true"><circle cx="7" cy="7" r="7" fill="var(--red)"/><circle cx="7" cy="7" r="3.6" fill="none" stroke="#fff" stroke-width="1"/><path d="M3.4 7h7.2M7 3.4c-1.6 2-1.6 5.2 0 7.2M7 3.4c1.6 2 1.6 5.2 0 7.2" fill="none" stroke="#fff" stroke-width="0.8"/></svg>
        <span>www.yourwebsite.com</span>
      </li>
    </ul>
  </section>

  <section class="card card--brand">
    <div class="brand-mark">
      <span class="brand-mark__dot"></span>
      <span class="brand-mark__name">Harbor Ledger</span>
    </div>
  </section>
</body>
</html>
```